Design a styled business card for an intimacy and attachment psychologist

I am a Psychologist providing online therapy to patients across the United States. My work is interpersonal and emotion-focused, with an emphasis on the client-therapist relationship. My primary areas of work are very personal, including sexuality and gender, abuse and trauma, and grief and loss. My target audience will be adults of all ages 18+.
My business card should convey a warm and inviting feeling of professionalism that is also casual and comfortable.
The front should be fairly simple and professional, consisting of:
- My name, Dr. Rosalind Petrakis
- My title, Licensed Psycholigist
- My logo
On either the front or the back, my contact information should be listed:
- ros@drrospetrakis.example
- 555.014.7788
- drrospetrakis.example
On the rear, I would like a description of the areas that I specialize in. This can be formatted in any way that appears stylistically interesting.
Individual and Couples
Relationships and Infidelity
Sexual Health & Aging
Gender Identity & Sexual Orientation
Abuse and Trauma
Sexual Compulsivity & Addiction
Sexual Dysfunction
Target Market(s)
My target audience will be adults of all ages 18+.
Industry/Entity Type
Psychology
Contact Information for Business Card
The front should be fairly simple and professional, consisting of: - My name, Dr. Rosalind Petrakis - My title, Licensed Psycholigist - My logo On either the front or the back, my contact information should be listed: - ros@drrospetrakis.example - 555.014.7788 - drrospetrakis.example On the rear, I would like a description of the areas that I specialize in. This can be formatted in any way that appears stylistically interesting. Individual and Couples Relationships and Infidelity Sexual Health & Aging Gender Identity & Sexual Orientation Abuse and Trauma Sexual Compulsivity & Addiction Sexual Dysfunction
- Follow brand guide

```html
<!DOCTYPE html>
<html lang="en">
<head>
<meta charset="utf-8">
<title>Dr. Rosalind Petrakis — Business Card</title>
<link rel="stylesheet" href="https://fonts.googleapis.com/css2?family=EB+Garamond:wght@400;600&display=swap">
<style>
  :root {
    --navy: #262046;
    --orange: #e8961e;
    --teal: #5bbfa5;
    --teal-light: #a9d8cc;
    --coral: #e56a5a;
    --paper: #ffffff;
    --backdrop: #e9e5df;
    --ink-soft: #3a3552;
  }
  * { box-sizing: border-box; margin: 0; padding: 0; }
  html, body {
    width: 1200px; height: 900px; overflow: hidden;
    background: var(--backdrop);
    font-family: "EB Garamond", Georgia, serif;
  }
  .canvas { position: relative; width: 1200px; height: 900px; }
  .card {
    position: absolute; left: 290px; width: 620px; height: 354px;
    border-radius: 28px; overflow: hidden;
    box-shadow: 0 10px 28px rgba(0,0,0,0.18);
  }
  /* Specialties side */
  .card--specialties { top: 60px; background: var(--paper); }
  .identity {
    position: absolute; left: 0; top: 0; width: 245px; height: 100%;
    display: flex; flex-direction: column; align-items: center; justify-content: center; gap: 18px;
  }
  .identity__mark {
    width: 96px; height: 96px; border-radius: 50%; background: var(--teal);
  }
  .identity__name {
    font-size: 25px; font-weight: 600; color: var(--navy);
    text-transform: uppercase; letter-spacing: 1px; line-height: 1.1; text-align: center;
  }
  .divider {
    position: absolute; top: 62px; width: 1px; height: 230px;
  }
  .card--specialties .divider { left: 258px; background: var(--coral); }
  .specialties { position: absolute; left: 288px; top: 64px; }
  .specialties__title {
    font-size: 17px; font-weight: 600; color: var(--orange);
    letter-spacing: 1.5px; text-transform: uppercase; margin-bottom: 6px;
  }
  .specialties__list { list-style: none; }
  .specialties__item {
    display: flex; align-items: center; gap: 9px;
    font-size: 16.5px; color: var(--ink-soft); line-height: 26px;
  }
  .bullet {
    width: 11px; height: 11px; border-radius: 50%;
    border: 1.5px solid var(--teal); flex: none;
  }
  /* Contact side */
  .card--contact { top: 486px; background: var(--navy); }
  .card--contact .identity { width: 270px; }
  .card--contact .identity__mark {
    width: 180px; height: 180px; background: var(--teal-light);
    border: 5px solid var(--paper);
  }
  .card--contact .divider { left: 282px; background: var(--teal); }
  .contact { position: absolute; left: 312px; top: 92px; color: var(--paper); }
  .contact__name {
    font-size: 22px; font-weight: 600; color: var(--orange);
    text-transform: uppercase; letter-spacing: 0.5px;
  }
  .contact__title { font-size: 18px; margin-bottom: 26px; }
  .contact__list { list-style: none; }
  .contact__item {
    display: flex; align-items: center; gap: 10px;
    font-size: 17px; line-height: 28px;
  }
  .contact__icon { width: 16px; height: 16px; flex: none; }
</style>
</head>
<body>
<main class="canvas">

  <section class="card card--specialties">
    <div class="identity">
      <div class="identity__mark"></div>
      <div class="identity__name">Dr. Rosalind<br>Petrakis</div>
    </div>
    <div class="divider"></div>
    <div class="specialties">
      <h2 class="specialties__title">Specialize In</h2>
      <ul class="specialties__list">
        <li class="specialties__item"><span class="bullet"></span>Stylistically Interesting</li>
        <li class="specialties__item"><span class="bullet"></span>Individual And Couples</li>
        <li class="specialties__item"><span class="bullet"></span>Relationships And Infidelity</li>
        <li class="specialties__item"><span class="bullet"></span>Sexual Health &amp; Aging</li>
        <li class="specialties__item"><span class="bullet"></span>Gender Identity &amp; Sexual Orientation</li>
        <li class="specialties__item"><span class="bullet"></span>Abuse And Trauma</li>
        <li class="specialties__item"><span class="bullet"></span>Sexual Compulsivity &amp; Addiction</li>
        <li class="specialties__item"><span class="bullet"></span>Sexual Dysfunction</li>
      </ul>
    </div>
  </section>

  <section class="card card--contact">
    <div class="identity">
      <div class="identity__mark"></div>
    </div>
    <div class="divider"></div>
    <div class="contact">
      <h1 class="contact__name">Dr. Rosalind Petrakis</h1>
      <p class="contact__title">Licensed Psycholigist</p>
      <ul class="contact__list">
        <li class="contact__item">
          <svg class="contact__icon" viewBox="0 0 16 16"><path fill="#e8961e" d="M3 2h3l1.5 3.5-2 1.2a8 8 0 0 0 3.8 3.8l1.2-2L14 10v3a1 1 0 0 1-1 1A11 11 0 0 1 2 3a1 1 0 0 1 1-1z"/></svg>
          555.014.7788
        </li>
        <li class="contact__item">
          <svg class="contact__icon" viewBox="0 0 16 16"><rect x="1.5" y="3.5" width="13" height="9" rx="1" fill="#e8961e"/><path d="M2 4.5l6 4.5 6-4.5" fill="none" stroke="#262046" stroke-width="1.2"/></svg>
          ros@drrospetrakis.example
        </li>
        <li class="contact__item">
          <svg class="contact__icon" viewBox="0 0 16 16"><circle cx="8" cy="8" r="6.5" fill="none" stroke="#e8961e" stroke-width="1.5"/><ellipse cx="8" cy="8" rx="2.8" ry="6.5" fill="none" stroke="#e8961e" stroke-width="1.2"/><path d="M1.5 8h13" stroke="#e8961e" stroke-width="1.2"/></svg>
          www.drrospetrakis.example
        </li>
      </ul>
    </div>
  </section>

</main>
</body>
</html>
```